Company Brochure - Recruitment Agency

We need a company brochure. We are a recruitment firm and we want to depict a professional, energetic and result oriented image. We would like our brochure to be in line with our logo design. A color filled and modern design will be a big plus.

We want the brochure to be smaller than a A4 size paper, elongated in shape with 3 pages on each side (see attached pics)
Updates

Reason: Need more designs to compare. Did not like the ones I received so far.

Target Market(s)

Big Corporations and Global Multinational companies

Industry/Entity Type

It Company

Requirements
Must have
• 6 long-sided Pages Design (with 3 Pages on each side)
• Page Measurement: 26cm x 14cm (for each page)
• Brochure Measurement: 26cm x 14 cm (when folded)
Nice to have
• Theme in line with our logo design.
• Project a fast, energetic and professional image.
Should not have
• Am open at this moment

```html
<!DOCTYPE html>
<html lang="en">
<head>
<meta charset="utf-8">
<title>SwiftTalent Brochure</title>
<link href="https://fonts.googleapis.com/css2?family=Open+Sans:wght@400;600;700;800&display=swap" rel="stylesheet">
<style>
:root{
  --green:#3cb54a;
  --green-dark:#24913a;
  --green-light:#7dd36a;
  --ink:#2e3338;
  --grey:#6b7075;
  --paper:#ffffff;
  --bg:#e8e9eb;
  --sky-top:#cfd8de;
  --sky-bottom:#8d9aa3;
}
*{box-sizing:border-box;margin:0;padding:0}
html,body{width:853px;height:1200px;overflow:hidden}
body{background:var(--bg);font-family:"Open Sans",Arial,sans-serif;color:var(--ink);position:relative}
.spread{position:absolute;left:36px;width:780px;height:480px;display:flex;box-shadow:0 2px 8px rgba(0,0,0,.12)}
.spread--outside{top:60px}
.spread--inside{top:650px}
.panel{width:260px;height:480px;position:relative;overflow:hidden;background:var(--paper)}
.panel + .panel{border-left:1px solid rgba(0,0,0,.06)}
.panel--green{background:linear-gradient(165deg,var(--green-light) 0%,var(--green) 45%,var(--green-dark) 100%);color:#fff}

/* outside: services panel */
.services{padding:26px 22px}
.services h3{font-size:9px;font-weight:700;margin:0 0 3px}
.services p{font-size:6.5px;line-height:1.5;margin-bottom:12px;opacity:.95}
.waves{position:absolute;left:0;bottom:0;width:260px;height:140px}

/* outside: mailing panel */
.mailing{display:flex;align-items:center;justify-content:center}
.mailing__address{transform:rotate(90deg);font-size:6.5px;color:var(--grey);line-height:1.6;white-space:nowrap;text-align:left}

/* cover */
.brand{display:flex;align-items:center;gap:5px;font-weight:800;color:var(--green);font-size:17px;letter-spacing:-.2px}
.brand__dot{width:10px;height:10px;border-radius:50%;background:var(--green)}
.cover .brand{position:absolute;left:96px;top:28px}
.cover__photo{position:absolute;left:0;bottom:0;width:260px;height:270px;background:linear-gradient(180deg,var(--sky-top) 0%,#b6c1c8 55%,var(--sky-bottom) 100%)}
.cover__tagline{position:absolute;left:90px;top:130px;width:160px;background:var(--green);color:#fff;padding:10px 12px;font-size:10.5px;font-weight:700;line-height:1.25;text-transform:uppercase}

/* inside: company */
.company__photo{height:190px;background:linear-gradient(135deg,#e9eef0 0%,#c9d3d8 60%,#a9b6bd 100%)}
.company__body{padding:22px 22px}
.company__body h2{font-size:14px;font-weight:700;margin-bottom:8px}
.company__body p{font-size:7px;line-height:1.6}

/* inside: lists */
.info{padding:30px 24px}
.info h3{color:var(--green);font-size:9.5px;font-weight:700;margin-bottom:5px}
.info ul{list-style:none;margin-bottom:16px}
.info li{font-size:7px;line-height:1.7;color:var(--ink);padding-left:9px;position:relative}
.info li::before{content:"";position:absolute;left:0;top:4px;width:4px;height:4px;background:var(--green);border-radius:50%}
.info p{font-size:7px;line-height:1.6;color:var(--grey);margin-bottom:16px}
.rule{height:1px;background:var(--green);opacity:.5;margin:0 0 14px}
.question{position:absolute;right:30px;top:205px;font-size:120px;font-weight:800;color:var(--green);line-height:1}
.contact{position:absolute;left:24px;top:345px;width:200px}
.contact h3{color:var(--green);font-size:9.5px;font-weight:700;margin-bottom:4px}
.contact p{font-size:7px;color:var(--grey);line-height:1.6}
.back .brand{position:absolute;right:24px;bottom:44px;font-size:14px}
.back__web{position:absolute;left:0;right:0;bottom:16px;text-align:center;font-size:7px;color:var(--grey);border-top:1px solid var(--green);margin:0 24px;padding-top:6px}
</style>
</head>
<body>

<section class="spread spread--outside">
  <div class="panel panel--green services">
    <h3>Our Recruitment Process</h3>
    <p>We listen first, map your needs and deliver shortlisted candidates who fit your culture and goals.</p>
    <h3>Talent Sourcing</h3>
    <p>A wide network of IT professionals ready to join global teams at short notice.</p>
    <h3>Executive Search</h3>
    <p>Discreet search for senior leaders who drive growth across regions and markets.</p>
    <h3>Contract Staffing</h3>
    <p>Flexible specialists for projects of any size, from quick fixes to long programmes.</p>
    <h3>Why Choose Us</h3>
    <p>Fast response, honest advice and results measured by lasting placements.</p>
    <svg class="waves" viewBox="0 0 260 140" aria-hidden="true">
      <path d="M0 60 C70 20 150 110 260 50 L260 140 L0 140Z" fill="#ffffff" opacity=".12"/>
      <path d="M0 95 C80 55 170 135 260 85 L260 140 L0 140Z" fill="#ffffff" opacity=".15"/>
    </svg>
  </div>
  <div class="panel mailing">
    <div class="mailing__address">SwiftTalent Consulting<br>14 Harbour Lane, Suite 5<br>Riverton</div>
  </div>
  <div class="panel cover">
    <div class="brand"><span class="brand__dot"></span>SwiftTalent</div>
    <div class="cover__photo" role="img" aria-label="City skyline with a businessman standing on a rooftop"></div>
    <div class="cover__tagline">Our team of specialist consultants in your project field</div>
  </div>
</section>

<section class="spread spread--inside">
  <div class="panel panel--green company">
    <div class="company__photo" role="img" aria-label="Businessman's hand reaching out for a handshake"></div>
    <div class="company__body">
      <h2>Our Company</h2>
      <p>SwiftTalent is an independent recruitment partner for technology firms. We connect big corporations and global multinationals with skilled people, quickly and with care. Our consultants know the market and stay with you after every hire.</p>
    </div>
  </div>
  <div class="panel info">
    <h3>Permanent Hiring</h3>
    <ul><li>Role profiling</li><li>Candidate screening</li><li>Interview support</li><li>Offer management</li></ul>
    <div class="rule"></div>
    <h3>IT Specialists</h3>
    <ul><li>Software developers</li><li>Network engineers</li><li>Data analysts</li><li>Project managers</li></ul>
    <div class="rule"></div>
    <h3>Our Approach</h3>
    <p>Clear timelines, regular updates and a single point of contact from brief to start date.</p>
  </div>
  <div class="panel info back">
    <h3>Industries</h3>
    <ul><li>Banking and finance</li><li>Telecom</li><li>Healthcare</li><li>Energy</li></ul>
    <h3>Our Values</h3>
    <ul><li>Speed</li><li>Integrity</li><li>Results</li></ul>
    <div class="question">?</div>
    <div class="contact">
      <h3>Have a question?</h3>
      <p>Call +00 123 456 789 or write to hello@swifttalent.example</p>
    </div>
    <div class="brand"><span class="brand__dot"></span>SwiftTalent</div>
    <div class="back__web">www.swifttalent.example</div>
  </div>
</section>

</body>
</html>
```